KVR Associates needs a web site

We need a web site for www.kvrassociates-example.com. KVR is a mergers and acquisition consulting company that focuses our buyer and seller services on logistics companies. We help put companies together, and help with legal and financial due diligence. We want the web site to express our service and show the logistics components. We want personalized images versus pictures of trucks and airplanes.

Our new logo uses Burgandy and grey colors. Image attached. We are not in to bold, big letters...classy, artistic, low key preferred. Confidentiality, experience, professional are what we want to express on the site.

All we expect for the first part of this project is a home page, and one subpage.  We are budgeting other funds for the technical aspects of the web site

Reason: All that I'm seeing so far is trucks, forklifts and planes. We are a legal mergers and acquisitions firm that focus on logistics. I like some of the images to say logistics, but really want it say legal, financial, and putting companies together. Will pay extra for the sub page if someone can impress us with a home page.

Reason: Swamped with another project at the moment...will work on this over the weekend and provide designer feedback and select final design by Tuesday

```html
<!DOCTYPE html>
<html lang="en">
<head>
<meta charset="utf-8">
<title>KVR Associates</title>
<link href="https://fonts.googleapis.com/css2?family=Open+Sans:wght@300;400;600&display=swap" rel="stylesheet">
<style>
  :root {
    --page-bg: #eeeeee;
    --ink: #222222;
    --body-text: #666666;
    --muted: #8a8a8a;
    --faint: #b4b4b4;
    --burgundy: #9b1b34;
    --nav-top: #5a5a5a;
    --nav-bottom: #2c2c2c;
    --rule: #cfcfcf;
    --card-line: #bdbdbd;
    --white: #ffffff;
    --footer: #464646;
  }
  * { box-sizing: border-box; margin: 0; padding: 0; }
  html, body { width: 930px; height: 1200px; overflow: hidden; }
  body {
    background: var(--page-bg);
    font-family: "Open Sans", Arial, sans-serif;
    color: var(--ink);
    position: relative;
  }
  .site { position: absolute; left: 86px; top: 0; width: 760px; height: 1200px; }

  /* Header */
  .brand {
    position: absolute; left: 0; top: 28px;
    display: flex; align-items: center; gap: 10px;
    font-size: 26px; font-weight: 400; color: var(--burgundy); letter-spacing: 0.5px;
  }
  .brand-mark { width: 14px; height: 14px; background: var(--burgundy); }
  .search { position: absolute; left: 571px; top: 33px; display: flex; gap: 7px; }
  .search-field {
    width: 140px; height: 22px; background: var(--white); border: 1px solid #c6c6c6;
    font-size: 9.5px; color: #a0a0a0; padding: 4px 7px;
  }
  .search-button {
    width: 31px; height: 22px; background: var(--white); border: 1px solid #c6c6c6;
    display: flex; align-items: center; justify-content: center;
  }

  /* Navigation */
  .main-nav {
    position: absolute; left: 0; top: 85px; width: 760px; height: 36px;
    background: linear-gradient(var(--nav-top), var(--nav-bottom));
    display: flex; align-items: center;
  }
  .main-nav a {
    height: 36px; display: flex; align-items: center; justify-content: center;
    color: #d6d6d6; font-size: 11.5px; text-decoration: none;
    border-right: 1px solid #222; box-shadow: 1px 0 0 #666;
  }
  .main-nav a.is-current { color: var(--white); }
  .call-now { margin-left: auto; padding-right: 12px; color: var(--white); font-size: 11.5px; font-weight: 600; }

  /* Hero */
  .hero {
    position: absolute; left: 0; top: 140px; width: 760px; height: 350px;
    background: linear-gradient(100deg, #0b2f55 0%, #165d97 35%, #2b86cc 58%, #5a8fc6 80%, #b9a6c8 100%);
    border: 1px solid #cfcfcf; overflow: hidden;
  }
  .hero-visual {
    position: absolute; right: 0; top: 0; width: 440px; height: 348px;
    background:
      radial-gradient(ellipse at 92% 10%, rgba(255,225,235,0.55), rgba(255,225,235,0) 35%),
      radial-gradient(ellipse at 50% 60%, rgba(30,50,90,0.45), rgba(30,50,90,0) 60%),
      linear-gradient(160deg, rgba(190,40,60,0) 40%, rgba(190,40,60,0.18) 60%, rgba(190,40,60,0) 75%);
  }
  .hero-copy { position: absolute; left: 37px; top: 88px; width: 350px; color: var(--white); }
  .hero-copy h1 { font-size: 25px; font-weight: 400; margin-bottom: 5px; white-space: nowrap; }
  .hero-copy p { font-size: 10.6px; line-height: 23px; font-weight: 300; }
  .read-more {
    display: inline-block; margin-top: 14px; background: #4a4a4a; color: var(--white);
    font-size: 12px; line-height: 16px; padding: 5px 9px; white-space: nowrap;
  }

  /* Services */
  .service {
    position: absolute; top: 518px; width: 171px; height: 263px;
    background: var(--white); border: 1px solid var(--card-line); padding: 8px;
  }
  .service-photo { width: 153px; height: 129px; }
  .service h2 { font-size: 11.5px; font-weight: 400; color: #333; margin: 14px 5px 0; }
  .service hr { border: 0; border-top: 1px solid #d8d8d8; margin: 9px 0 11px; }
  .service p { font-size: 10px; line-height: 18.5px; color: var(--muted); padding: 0 5px; }

  .section-rule { position: absolute; left: 0; top: 830px; width: 760px; border-top: 1px solid var(--rule); }

  /* Welcome */
  .welcome { position: absolute; left: 0; top: 864px; width: 436px; }
  .welcome h2 { font-size: 19.5px; font-weight: 400; margin-bottom: 24px; }
  .welcome h2 span { color: var(--burgundy); }
  .welcome p { font-size: 10.9px; line-height: 18.6px; color: var(--body-text); font-weight: 300; }
  .column-rule { position: absolute; left: 455px; top: 866px; height: 276px; border-left: 1px solid var(--rule); }

  /* Testimonials */
  .testimonials { position: absolute; left: 493px; top: 864px; width: 265px; }
  .testimonials h2 { font-size: 19.5px; font-weight: 400; margin-bottom: 24px; }
  .quote-box { background: var(--white); border: 1px solid #e0e0e0; border-radius: 4px; height: 167px; position: relative; }
  .quote-box p { font-size: 10.2px; line-height: 18.6px; color: var(--faint); padding: 22px 23px 0; height: 125px; }
  .quote-author {
    display: flex; justify-content: space-between; border-top: 1px solid #e4e4e4;
    background: #f6f6f6; height: 40px; padding: 10px 11px 0 15px; font-size: 10px; color: #333;
    border-radius: 0 0 4px 4px;
  }
  .quote-pointer {
    position: absolute; left: 122px; bottom: -9px; width: 0; height: 0;
    border-left: 8px solid transparent; border-right: 8px solid transparent; border-top: 9px solid #e0e0e0;
  }
  .client-photo {
    position: absolute; left: 99px; top: 234px; width: 56px; height: 56px; border-radius: 50%;
    background: radial-gradient(circle, #b7bfca, #5b6a80); border: 3px solid var(--white);
    box-shadow: 0 0 3px rgba(0,0,0,0.25);
  }

  /* Footer */
  .site-footer {
    position: absolute; left: 0; top: 1167px; width: 760px; height: 31px; background: var(--footer);
    color: #dddddd; font-size: 10px; text-align: center; line-height: 31px;
  }
</style>
</head>
<body>
<div class="site">
  <header>
    <div class="brand"><span class="brand-mark"></span>KVR Associates</div>
    <div class="search">
      <div class="search-field">Search...</div>
      <div class="search-button">
        <svg width="10" height="10" viewBox="0 0 10 10"><circle cx="4" cy="4" r="3" fill="none" stroke="#999" stroke-width="1.3"/><line x1="6.3" y1="6.3" x2="9" y2="9" stroke="#999" stroke-width="1.4"/></svg>
      </div>
    </div>
  </header>

  <nav class="main-nav">
    <a class="is-current" style="width:70px">Home</a>
    <a style="width:91px">About Us</a>
    <a style="width:94px">Legal Help</a>
    <a style="width:118px">Financial Help</a>
    <a style="width:93px">Contact Us</a>
    <span class="call-now">Call Us Now: 555 014 2030</span>
  </nav>

  <section class="hero">
    <div class="hero-visual" role="img" aria-label="Businessman with a lightbulb head climbing coin stacks beside a rising red arrow, an airplane and a connected world map"></div>
    <div class="hero-copy">
      <h1>KVR Associates</h1>
      <p>KVR assists business owners within the logistics industry to implement growth and exit strategies. We offer business planning and merger and acquisition(M&amp;A) advisory services.</p>
      <span class="read-more">Read More</span>
    </div>
  </section>

  <article class="service" style="left:0">
    <div class="service-photo" role="img" aria-label="Business people shaking hands at a meeting table" style="background:linear-gradient(135deg,#e4e6ea,#a9acb3 55%,#6e737c)"></div>
    <h2>M&amp;A Advisory Service</h2><hr>
    <p>Lorem ipsum dolor sit amet, consectetuer adipiscing elit, sed diam nonummy nibh</p>
  </article>
  <article class="service" style="left:197px">
    <div class="service-photo" role="img" aria-label="Team meeting around a conference table with a presenter" style="background:linear-gradient(170deg,#e3ebf2,#aebbc9 45%,#2f3238)"></div>
    <h2>Business Planing</h2><hr>
    <p>Lorem ipsum dolor sit amet, consectetuer adipiscing elit, sed diam nonummy nibh</p>
  </article>
  <article class="service" style="left:394px">
    <div class="service-photo" role="img" aria-label="Smiling businessman with colleagues in a bright office" style="background:linear-gradient(135deg,#edf1f4,#c3d0dc 50%,#8aa3bd)"></div>
    <h2>Your Growth Strategy</h2><hr>
    <p>Lorem ipsum dolor sit amet, consectetuer adipiscing elit, sed diam nonummy nibh</p>
  </article>
  <article class="service" style="left:588px">
    <div class="service-photo" role="img" aria-label="Two figures pushing large puzzle pieces together" style="background:radial-gradient(ellipse at 50% 40%,#9a9ea2,#5b6064)"></div>
    <h2>Logistics Consultancy</h2><hr>
    <p>Lorem ipsum dolor sit amet, consectetuer adipiscing elit, sed diam nonummy nibh</p>
  </article>

  <div class="section-rule"></div>

  <section class="welcome">
    <h2>Welcome To <span>KVR</span> Associates</h2>
    <p>KVR assists business owners within the logistics industry to implement growth and exit strategies. We offer business planning and merger and acquisition(M&amp;A) advisory services. KVR services are offered by industry executives with extensive M&amp;A experience. Your company will benefit from a unique and outside perspective from consultants that understand your business.</p>
    <p>KVR can help you formulate and execute your growth strategy. We take a strategic and consultative approach with our advisory services that will help you grow your business effectively.&nbsp; Since our experience and focus is only in the logistics space, you can be confident that our process will be efficient and streamlined as we help achieve your goals.</p>
  </section>
  <div class="column-rule"></div>

  <section class="testimonials">
    <h2>Client Testimonials</h2>
    <div class="quote-box">
      <p>Lorem ipsum dolor sit amet, consectetuer adipiscing elit, sed diam nonummy nibh euismod tincidunt ut laoreet dolore magna aliquam erat volutpat.</p>
      <div class="quote-author"><span>Dana Mercer</span><span>CEO Of Example</span></div>
      <span class="quote-pointer"></span>
    </div>
    <div class="client-photo" role="img" aria-label="Client portrait"></div>
  </section>

  <footer class="site-footer">Copyright 2014. KVR ASSOCIATES. All rights reserved.</footer>
</div>
</body>
</html>
```